PageForge Design Project for lornabethwickes.com.au

Update
PLEASE NOTE ...Coding Required

I need a simple website to display my art. There will be 4 different categories - FloraGrandis (botanical art), Oceanlife, Travel Sketchbook, Portraits. There needs to be room for an introduction to me and my work,photos of my studio and views from here and a description of each individual piece. I will probably display no more than 10 pieces in category. Obviously I need to change photos on a regular basis.

I would also like to include a CoinPort button to be connected to my CoinPort account.

I have already started to do a website on PageForge but am finding it too hard to do.

Thank you

Lorna
Updates

Reason: I have provided a deadline extension as I feel the initial lead up time could be too short. Hope that helps you. Lorna

Dear designers. Thankyou all so much for submitting some beautiful designs. I will spend time this weekend evaluating them but as the closing date is January 19, I will not make final decisions until then.  You have probably received an update by now butI  just want to mention that Coding is required.

Cheers

Lorna

Thank you Designers for your patience.  I have been advised by ArtistHive that I cannot make a decision until the deadline has passed, so will let you know on Saturday.

Thank you.
Lorna.

Target Market(s)

35 to 75 who want to buy art and very personal gifts

Industry/Entity Type

Travel

Requirements
Must have
• Ability to change photos often. Modern, elegant, streamlined
Nice to have
• The colour green, an elegant font - sans serif and definitely not courier; room for a photo of me (maybe), and an interesting headline font
Should not have
• quirky, cartooney, retro.

```html
<!DOCTYPE html>
<html lang="en">
<head>
<meta charset="utf-8">
<title>Lorna Beth Wickes – FloraGrandis</title>
<link rel="stylesheet" href="https://fonts.googleapis.com/css2?family=Arimo:wght@400;700&family=Noto+Serif:ital,wght@0,400;1,400&family=Tinos&display=swap">
<style>
:root{
  --green:#9dc14a;
  --green-dark:#7fa63a;
  --btn-top:#96c050;
  --btn-bottom:#6f9a34;
  --magenta:#b5177a;
  --ink:#444;
  --ink-soft:#666;
  --bar:#2f2f2f;
  --bar-dark:#242424;
  --paper:#f4f4ee;
  --wood-a:#f0d6a6;
  --wood-b:#e6c48c;
}
*{margin:0;padding:0;box-sizing:border-box}
html,body{width:894px;height:1200px;overflow:hidden}
body{position:relative;font-family:Arimo,Arial,sans-serif;color:var(--ink);
  background:linear-gradient(90deg,var(--wood-a),var(--wood-b) 30%,var(--wood-a) 55%,var(--wood-b) 80%,var(--wood-a))}
.wood{position:absolute;inset:0}
.page{position:absolute;left:43px;top:0;width:808px;height:1161px;background:var(--paper);box-shadow:0 0 6px rgba(0,0,0,.2)}
.abs{position:absolute}
.topbar{left:0;top:0;width:808px;height:31px;background:var(--bar)}
.topbar .account{left:580px;top:9px;font-size:11px;font-weight:700;color:#999}
.topbar .cart{left:661px;top:0;width:147px;height:31px;background:var(--bar-dark);color:#fff;font-size:11px;font-weight:700}
.cart svg{position:absolute;left:45px;top:8px}
.cart span{position:absolute;left:69px;top:10px}
.header{left:0;top:31px;width:808px;height:88px;background:var(--green)}
.brand{left:38px;top:20px;display:flex;align-items:center;gap:10px;color:var(--magenta);font-family:Tinos,serif}
.brand .dot{width:40px;height:40px;border-radius:50%;background:var(--magenta)}
.brand .name{font-size:28px;line-height:26px}
.brand .sub{font-size:15px;line-height:16px;padding-left:120px}
.nav{left:382px;top:38px;display:flex;gap:0;font-family:Tinos,serif;font-size:13px;color:#fff}
.nav a{color:#fff;text-decoration:none;margin-right:39px}
.hero{left:0;top:119px;width:808px;height:371px;background:#fff}
.hero h1{left:35px;top:31px;font-size:20px;color:var(--green);font-weight:700}
.hero .tag{left:35px;top:61px;font-family:"Noto Serif",serif;font-style:italic;font-size:8px;color:#999}
.hero .lede{left:35px;top:96px;width:290px;font-size:10px;line-height:17px;color:#555}
.hero .price{left:35px;top:160px;font-size:28px;font-weight:700;color:#444}
.btn{background:linear-gradient(var(--btn-top),var(--btn-bottom));color:#fff;border-radius:3px;text-align:center;box-shadow:0 1px 2px rgba(0,0,0,.25)}
.hero .buy{left:35px;top:218px;width:268px;height:46px;line-height:46px;font-size:23px;font-weight:700}
.hero .art{left:550px;top:0;width:258px;height:371px;background:radial-gradient(circle at 55% 35%,#f08a78,#f4b9a8 35%,#eeeaea 70%,#e4e4e4)}
.arrow{width:36px;height:33px;background:#333;border-radius:2px;top:330px}
.arrow svg{position:absolute;left:13px;top:11px}
.stripes{left:0;width:808px;height:10px;background:repeating-linear-gradient(45deg,#e9e9e2 0 2px,#f4f4ee 2px 5px)}
.latest h2{left:35px;top:528px;font-size:15px;font-weight:400;color:var(--green)}
.card{top:573px;width:234px;height:424px;background:#fff;border:1px solid #e2e2dc}
.card .photo{left:0;top:0;width:232px;height:172px}
.card h3{left:12px;top:187px;font-size:13px;font-weight:700;color:#333}
.card p{left:12px;top:206px;width:212px;font-family:"Noto Serif",serif;font-style:italic;font-size:10px;line-height:16.3px;color:#555}
.card .cost{left:32px;top:389px;font-size:15px;font-weight:700;color:#444}
.card .add{left:128px;top:376px;width:94px;height:35px;line-height:35px;font-size:14px}
.card .rule{left:0;top:419px;width:94px;height:3px;background:#ddd}
.welcome{left:35px;top:1056px;font-family:"Noto Serif",serif;font-style:italic;font-size:20px;line-height:25px;color:#444}
.browse{left:573px;top:1058px;width:200px;height:47px;line-height:47px;font-size:19px}
.footer{left:0;top:1133px;width:808px;height:28px;background:#262626}
.copyright{left:43px;top:1172px;width:186px;height:28px;background:var(--green);font-family:Tinos,serif;font-size:9px;color:#fff;line-height:30px;padding-left:12px}
.copyright span{color:#e7f2c6}
</style>
</head>
<body>
<div class="wood" role="img" aria-label="Light wood grain background"></div>
<div class="page">
  <div class="abs topbar">
    <span class="abs account">My Account</span>
    <div class="abs cart">
      <svg width="16" height="14" viewBox="0 0 16 14" fill="none" stroke="#fff" stroke-width="1.5"><path d="M1 1h3l2 8h8l1.5-6H5"/><circle cx="7" cy="12" r="1.2"/><circle cx="13" cy="12" r="1.2"/></svg>
      <span>0 items</span>
    </div>
  </div>
  <header class="abs header">
    <div class="abs brand">
      <div class="dot"></div>
      <div><div class="name">Lorna Beth Wickes</div><div class="sub">FloraGrandis</div></div>
    </div>
    <nav class="abs nav"><a>HOME</a><a>BLOG</a><a>SHOP</a><a>CHECKOUT</a><a>CONTACT</a></nav>
  </header>
  <section class="abs hero">
    <h1 class="abs">Australian Orchid</h1>
    <p class="abs tag">This is a beautiful design...etc</p>
    <p class="abs lede">Lorem ipsum dolor sit amet, consectetur adipiscing elit. Vestibulum semper diam ut dolor commodo pellentesque. Nullam diam nibh, porttitor eu aliquam nec,</p>
    <div class="abs price">49.99</div>
    <div class="abs btn buy">Buy Now</div>
    <div class="abs art" role="img" aria-label="Watercolour painting of a coral-red orchid with small blossoms on a branch"></div>
    <div class="abs arrow" style="left:694px"><svg width="8" height="10" viewBox="0 0 8 10"><path d="M6 1L2 5l4 4" stroke="#fff" stroke-width="2" fill="none"/></svg></div>
    <div class="abs arrow" style="left:737px"><svg width="8" height="10" viewBox="0 0 8 10"><path d="M2 1l4 4-4 4" stroke="#fff" stroke-width="2" fill="none"/></svg></div>
  </section>
  <div class="abs stripes" style="top:490px"></div>
  <section class="latest">
    <h2 class="abs">LATEST ITEMS</h2>
    <article class="abs card" style="left:35px">
      <div class="abs photo" role="img" aria-label="Botanical painting of pink frangipani flowers with long green leaves" style="background:linear-gradient(135deg,#5e8a4a,#a9c18e 45%,#f3e6ec 75%,#fff)"></div>
      <h3 class="abs">Purple Harts</h3>
      <p class="abs">Lorem ipsum dolor sit amet, consectetur adipiscing elit. Vestibulum semper diam ut dolor commodo pellentesque. Nullam diam nibh, porttitor eu aliquam nec, hendrerit in dolor. Nullam eu nisl vitae eros posuere facilisis. Cras a urna venenatis libero euismod pellentesque a ut dui. Integer placerat posuere malesuada. Phasellus laoreet est laoreet mauris vehicula vitae convallis nisi pharetra.</p>
      <div class="abs cost">$199.95</div>
      <div class="abs btn add">Add to cart</div>
      <div class="abs rule"></div>
    </article>
    <article class="abs card" style="left:287px">
      <div class="abs photo" role="img" aria-label="Watercolour of white daisies against pale green leaves" style="background:radial-gradient(circle at 45% 40%,#f4f4ec,#c9d6bd 55%,#8fa97f)"></div>
      <h3 class="abs">Venus Trap</h3>
      <p class="abs">Lorem ipsum dolor sit amet, consectetur adipiscing elit. Vestibulum semper diam ut dolor commodo pellentesque. Nullam diam nibh, porttitor eu aliquam nec, hendrerit in dolor. Nullam eu nisl vitae eros posuere facilisis. Cras a urna venenatis libero euismod pellentesque a ut dui. Integer placerat posuere malesuada. Phasellus laoreet est laoreet mauris vehicula vitae convallis nisi pharetra.</p>
      <div class="abs cost">$79.95</div>
      <div class="abs btn add">Add to cart</div>
      <div class="abs rule"></div>
    </article>
    <article class="abs card" style="left:538px">
      <div class="abs photo" role="img" aria-label="Watercolour painting of a coral-red orchid" style="background:radial-gradient(circle at 50% 25%,#f08a78,#f4b9a8 40%,#f1eeee 75%)"></div>
      <h3 class="abs">Australian Orchid</h3>
      <p class="abs">Lorem ipsum dolor sit amet, consectetur adipiscing elit. Vestibulum semper diam ut dolor commodo pellentesque. Nullam diam nibh, porttitor eu aliquam nec, hendrerit in dolor. Nullam eu nisl vitae eros posuere facilisis. Cras a urna venenatis libero euismod pellentesque a ut dui. Integer placerat posuere malesuada. Phasellus laoreet est laoreet mauris vehicula vitae convallis nisi pharetra.</p>
      <div class="abs cost">$99.95</div>
      <div class="abs btn add">Add to cart</div>
      <div class="abs rule"></div>
    </article>
  </section>
  <div class="abs stripes" style="top:1018px"></div>
  <p class="abs welcome">Welcome to Lorna Beth Wickes and FloraGrandis,<br>Hope you enjoy my art....see you soon!</p>
  <div class="abs btn browse">Browse shop</div>
  <footer class="abs footer"></footer>
</div>
<div class="abs copyright">COPYRIGHT 2013 - <span>LORNA BETH WICKES</span></div>
</body>
</html>
```